Business cards

We need business cards for the logo that you designed for our company. Something simple and clean.

Target Market(s)

Homeowners/ people looking for construction work

Industry/Entity Type

Construction

Contact Information for Business Card

Name: Dana Holbrit, Number: 602-547-9164, Email: HolbritBuildingGroup@mailvesta.com ROC# 846203

Font styles to use
Serif

Colors

Designer to choose colors to be used in the design.

Requirements
Must have
• On one side of the card I would like to be all of the personal information I have put above along with the company logo that I have attached.
• On the other side of the card I would like the top half of the card to be the logo and then on the bottom half I would like to have the areas of construction we focus on along with an icon that represents it like the picture I have attached.
• Areas we focus on:
• Roofing, Kitchen and bath Remodel, Water Damage, Storm Damage, Fire Damage, Insurance Specialist
• If we could arrange those in alphabetical order.
Nice to have
• I have added 2 company logos a colorful one and a black one it would be nice to see a couple different options the black logo to be more simple and sleek and the colorful logo to be more colorful

```html
<!DOCTYPE html>
<html lang="en">
<head>
<meta charset="utf-8">
<title>Holbrit Building Group – Business Cards</title>
<link rel="stylesheet" href="https://fonts.googleapis.com/css2?family=Arimo:wght@400;700&family=Open+Sans:wght@600&display=swap">
<style>
  :root {
    --bg: #3b3431;
    --card-white: #ffffff;
    --card-dark: #1d1d1f;
    --tile: #343436;
    --blue: #2a9fd8;
    --red: #e5262b;
    --ink: #2b2b2b;
    --rule: #9a9a9a;
  }
  * { box-sizing: border-box; margin: 0; padding: 0; }
  html, body { width: 1200px; height: 844px; overflow: hidden; }
  body {
    background: var(--bg);
    font-family: "Arimo", Arial, sans-serif;
    position: relative;
  }
  .card {
    position: absolute;
    top: 272px;
    width: 525px;
    height: 300px;
    border-radius: 4px;
    box-shadow: 0 8px 24px rgba(0,0,0,.35);
  }

  /* Front */
  .card-front { left: 50px; background: var(--card-white); color: var(--ink); }
  .brand {
    position: absolute; right: 34px; top: 58px;
    display: flex; align-items: center; gap: 12px;
  }
  .brand-mark { width: 26px; height: 26px; background: var(--blue); }
  .brand-name {
    font-weight: 700; font-size: 25px; letter-spacing: 1px;
    color: var(--blue); text-transform: uppercase; line-height: 1;
  }
  .rule-top {
    position: absolute; left: 28px; right: 28px; top: 128px;
    border-top: 1px solid var(--rule);
  }
  .licence {
    position: absolute; right: 34px; top: 146px;
    font-size: 15px; color: #444;
  }
  .person {
    position: absolute; left: 34px; top: 206px;
    font-weight: 700; font-size: 22px; text-transform: uppercase; letter-spacing: .5px;
  }
  .person .first { color: var(--blue); }
  .person .last { color: var(--red); }
  .rule-name {
    position: absolute; left: 34px; width: 250px; top: 238px;
    border-top: 1px solid var(--rule);
  }
  .contact {
    position: absolute; left: 34px; top: 248px;
    list-style: none; font-size: 15px; color: #333; line-height: 22px;
  }
  .contact li { display: flex; align-items: center; gap: 8px; }
  .contact svg { width: 12px; height: 12px; fill: var(--blue); flex: none; }

  /* Back */
  .card-back { left: 625px; background: var(--card-dark); }
  .services {
    position: absolute; inset: 30px 20px 24px;
    display: grid; grid-template-columns: repeat(3, 1fr); grid-template-rows: 1fr 1fr;
    list-style: none;
  }
  .service { display: flex; flex-direction: column; align-items: center; justify-content: center; gap: 9px; }
  .service-tile {
    width: 64px; height: 64px; border-radius: 8px; background: var(--tile);
    display: flex; align-items: center; justify-content: center;
  }
  .service-tile svg { width: 36px; height: 36px; fill: var(--blue); stroke: var(--blue); }
  .service-label {
    font-family: "Open Sans", Arial, sans-serif; font-weight: 600;
    font-size: 11px; color: var(--red); text-transform: uppercase; text-align: center; line-height: 1.25;
  }
</style>
</head>
<body>

<section class="card card-front">
  <div class="brand">
    <span class="brand-mark"></span>
    <span class="brand-name">Holbrit Building Group</span>
  </div>
  <div class="rule-top"></div>
  <p class="licence">ROC# 846203</p>
  <h1 class="person"><span class="first">Dana</span> <span class="last">Holbrit</span></h1>
  <div class="rule-name"></div>
  <ul class="contact">
    <li>
      <svg viewBox="0 0 24 24" aria-hidden="true"><path d="M6.6 10.8a15 15 0 0 0 6.6 6.6l2.2-2.2a1 1 0 0 1 1-.25 11.4 11.4 0 0 0 3.6.57 1 1 0 0 1 1 1V20a1 1 0 0 1-1 1A17 17 0 0 1 3 4a1 1 0 0 1 1-1h3.5a1 1 0 0 1 1 1c0 1.25.2 2.45.57 3.57a1 1 0 0 1-.25 1z"/></svg>
      602-547-9164
    </li>
    <li>
      <svg viewBox="0 0 24 24" aria-hidden="true"><path d="M2 5h20v14H2z M3 6l9 7 9-7" fill="none" stroke="#2a9fd8" stroke-width="2"/><path d="M2 5h20L12 12z"/></svg>
      HolbritBuildingGroup@mailvesta.com
    </li>
  </ul>
</section>

<section class="card card-back">
  <ul class="services">
    <li class="service">
      <span class="service-tile"><svg viewBox="0 0 24 24" aria-hidden="true"><path stroke="none" d="M12 2c1 4 6 6 6 12a6 6 0 0 1-12 0c0-3 2-5 3-6 0 2 1 3 2 3 0-3-1-6 1-9z"/></svg></span>
      <span class="service-label">Fire Damage</span>
    </li>
    <li class="service">
      <span class="service-tile"><svg viewBox="0 0 24 24" aria-hidden="true"><path fill="none" stroke-width="2" d="M5 11l7-6 7 6M7 10v6h10v-6M3 16c2 3 5 5 9 5s7-2 9-5"/></svg></span>
      <span class="service-label">Insurance Specialist</span>
    </li>
    <li class="service">
      <span class="service-tile"><svg viewBox="0 0 24 24" aria-hidden="true"><path stroke="none" d="M3 12h18v2a5 5 0 0 1-5 5H8a5 5 0 0 1-5-5z"/><path fill="none" stroke-width="1.6" d="M6 12V5a2 2 0 0 1 4 0M7 19l-1 2M17 19l1 2"/></svg></span>
      <span class="service-label">Kitchen &amp;<br>Bath Remodel</span>
    </li>
    <li class="service">
      <span class="service-tile"><svg viewBox="0 0 24 24" aria-hidden="true"><path fill="none" stroke-width="2" d="M2 13l10-8 10 8"/><path stroke="none" d="M5 13l7-5.5 7 5.5v7H5z"/></svg></span>
      <span class="service-label">Roofing</span>
    </li>
    <li class="service">
      <span class="service-tile"><svg viewBox="0 0 24 24" aria-hidden="true"><path fill="none" stroke-width="1.8" d="M7 16a4 4 0 0 1 0-8 5 5 0 0 1 9.6-1A4 4 0 0 1 17 16z"/><path stroke="none" d="M12 13l-3 5h2.5l-1 4 4-6h-2.5l1.5-3z"/></svg></span>
      <span class="service-label">Storm Damage</span>
    </li>
    <li class="service">
      <span class="service-tile"><svg viewBox="0 0 24 24" aria-hidden="true"><path stroke="none" d="M12 3c2 4 6 8 6 12a6 6 0 0 1-12 0c0-4 4-8 6-12z"/></svg></span>
      <span class="service-label">Water Damage</span>
    </li>
  </ul>
</section>

</body>
</html>
```